ORVILMA card Technical Architecture

Hello everyone ORVILMA: It is a consulting firm in Architecture and Construction. I require a card duplexing, sober, elegant, classic but not boring. Update 1: Use the following data for the card. Name: Rodrigo Salinas Tomás Quevedo Position: COO Twitter: @orvilmaAT Homepage: orvilma.com home address not include the participation of all thank you.

Target Market(s)

Construction companies, Architects and Consulting Engineers

Industry/Entity Type

Consulting

Contact Information for Business Card

Los campos que debe tener:
Nombre, Cargo, email, homepage y twitter

Font styles to use
Serif
Sans Serif
Other font styles liked:
• Me gustan playfair display, open sans y roboto, pero estoy sujeto a sus propuestas

Requirements
Must have
• Colors: Present combined proposals in white, red, gray and black Update 1: The two names must be clearly differentiated from the two surnames
Nice to have
• They are free to present their best proposals. I will bring them immediate feedback to the extent you can go see their designs. Complete data for card and logo files will give the winner the

```html
<!DOCTYPE html>
<html lang="es">
<head>
<meta charset="utf-8">
<title>ORVILMA – Arquitectura Técnica</title>
<link rel="stylesheet" href="https://fonts.googleapis.com/css2?family=Montserrat:wght@300;400&family=Open+Sans:wght@400;600;700&display=swap">
<style>
  :root {
    --stage: #d9d9db;
    --card: #27272a;
    --card-edge: #1d1d20;
    --skyline: #202023;
    --white: #f4f4f4;
    --grey: #c9c9cc;
    --red: #c4161c;
    --red-line: #8e1418;
  }
  * { box-sizing: border-box; margin: 0; padding: 0; }
  html, body { width: 1200px; height: 900px; overflow: hidden; }
  body {
    background: var(--stage);
    display: flex;
    align-items: center;
    justify-content: center;
    gap: 40px;
    font-family: "Open Sans", sans-serif;
  }
  .card {
    position: relative;
    width: 540px;
    height: 310px;
    background: var(--card);
    border-radius: 24px;
    overflow: hidden;
    box-shadow: 0 6px 0 var(--card-edge), 0 14px 30px rgba(0,0,0,.25);
  }

  /* Back side: contact */
  .card-back .contact {
    position: absolute;
    top: 34px;
    left: 36px;
    color: var(--white);
  }
  .contact .person-name {
    font-size: 19px;
    line-height: 1.15;
    font-weight: 400;
  }
  .contact .surname-pair { display: block; }
  .contact .accent { color: var(--red); font-weight: 700; }
  .contact .role {
    margin-top: 6px;
    font-size: 12.5px;
    color: var(--grey);
  }
  .contact-list {
    list-style: none;
    margin-top: 16px;
    font-size: 13px;
    color: var(--white);
  }
  .contact-list li {
    display: flex;
    align-items: center;
    gap: 10px;
    line-height: 22px;
  }
  .contact-list svg { width: 13px; height: 13px; flex: none; }

  .skyline {
    position: absolute;
    left: 0;
    bottom: 0;
    width: 62%;
    height: 42%;
    background: linear-gradient(180deg, rgba(32,32,35,0) 0%, var(--skyline) 35%, var(--skyline) 100%);
  }
  .card-back .brand-mark {
    position: absolute;
    right: 40px;
    bottom: 92px;
    font-family: "Montserrat", sans-serif;
    font-weight: 400;
    font-size: 17px;
    letter-spacing: 4px;
    color: var(--red);
  }

  /* Front side: brand */
  .card-front .lockup {
    position: absolute;
    left: 0; right: 0;
    top: 108px;
    display: flex;
    flex-direction: column;
    align-items: center;
  }
  .lockup .brand-name {
    display: flex;
    align-items: center;
    gap: 18px;
    font-family: "Montserrat", sans-serif;
    font-weight: 300;
    font-size: 46px;
    letter-spacing: 14px;
    color: var(--white);
  }
  .lockup .brand-dot {
    width: 14px; height: 14px;
    border-radius: 50%;
    background: var(--red);
  }
  .lockup .rule {
    width: 360px;
    height: 1px;
    background: var(--red-line);
    margin: 10px 0 6px;
  }
  .lockup .tagline {
    font-size: 13px;
    letter-spacing: 5px;
    color: var(--red);
  }
</style>
</head>
<body>

  <section class="card card-back" aria-label="Reverso de la tarjeta">
    <div class="contact">
      <h1 class="person-name">
        <span class="given-pair">Tomás <span class="accent">Rodrigo</span></span>
        <span class="surname-pair">Salinas <span class="accent">Quevedo</span></span>
      </h1>
      <p class="role">Director de Operaciones</p>
      <ul class="contact-list">
        <li>
          <svg viewBox="0 0 16 16" aria-hidden="true"><circle cx="8" cy="8" r="7" fill="none" stroke="#c4161c" stroke-width="1.4"/><path d="M5.6 4.6l1.3 1.6-.7.9c.5 1 1.3 1.8 2.3 2.3l.9-.7 1.6 1.3-.8 1.2c-2.6-.4-4.6-2.4-5-5z" fill="#c4161c"/></svg>
          5550 218 734 (+570)
        </li>
        <li>
          <svg viewBox="0 0 16 16" aria-hidden="true"><circle cx="8" cy="8" r="7" fill="none" stroke="#c4161c" stroke-width="1.4"/></svg>
          @orvilmaAT
        </li>
        <li>
          <svg viewBox="0 0 16 16" aria-hidden="true"><circle cx="8" cy="8" r="7" fill="none" stroke="#c4161c" stroke-width="1.4"/><ellipse cx="8" cy="8" rx="2.6" ry="4.6" fill="none" stroke="#c4161c" stroke-width="1"/><line x1="3.4" y1="8" x2="12.6" y2="8" stroke="#c4161c" stroke-width="1"/></svg>
          orvilma.com
        </li>
      </ul>
    </div>
    <div class="skyline" role="img" aria-label="Silueta tenue de una ciudad con edificios altos"></div>
    <span class="brand-mark">ORVILMA</span>
  </section>

  <section class="card card-front" aria-label="Anverso de la tarjeta">
    <div class="lockup">
      <div class="brand-name">ORVILMA<span class="brand-dot"></span></div>
      <div class="rule"></div>
      <p class="tagline">ARQUITECTURA TÉCNICA</p>
    </div>
  </section>

</body>
</html>
```